Football blog needs a Wordpress design new site

We need a wordpress design for a new football blog site. We would like to see a design that uses the colours green, white and black and one that makes good use of the slideshow widgets as scene in the site 'www.trenvix.net'
We would like a modern and sleek looking site but one that is also professional and easy to navigate.
Unfortunately due to unforeseen circumstances we are having to shorten the deadline date for this project.
The new deadline date is 16/07/2014.
We apologise for any inconveniance
It Professional

```html
<!DOCTYPE html>
<html lang="en">
<head>
<meta charset="utf-8">
<title>Pitchside Talk – Football Blog</title>
<link href="https://fonts.googleapis.com/css2?family=Open+Sans:wght@400;600;700&display=swap" rel="stylesheet">
<style>
:root{
  --green:#3bb54a;
  --green-dark:#2a8f37;
  --black:#111;
  --panel:#2a2a2a;
  --panel-dark:#1e1e1e;
  --page:#ececec;
  --white:#fff;
  --text:#444;
  --muted:#888;
  --orange:#f27b1f;
  --blue:#2e86c8;
}
*{box-sizing:border-box;margin:0;padding:0}
html,body{width:780px;height:1200px;overflow:hidden}
body{position:relative;background:var(--page);font-family:"Open Sans",Arial,sans-serif;color:var(--text);font-size:6px;line-height:1.35}
.abs{position:absolute}
.hero-bg{left:0;top:0;width:780px;height:270px}
.topbar{left:0;top:0;width:780px;height:14px;background:var(--black)}
.topnav{left:196px;top:3px;display:flex;gap:16px;font-size:6px;color:#ccc}
.topnav .active{color:var(--green);border-bottom:1px solid var(--green)}
.social{right:203px;top:3px;display:flex;gap:2px}
.social span{width:9px;height:8px;background:#444;display:block}
.brand{left:200px;top:28px;display:flex;align-items:center;gap:4px}
.brand-dot{width:22px;height:22px;border-radius:50%;background:var(--black);border:2px solid var(--green)}
.brand-name{font-size:8px;font-weight:700;color:var(--green-dark)}
.panel{left:196px;top:79px;width:381px;height:317px;background:var(--panel);border-bottom:3px solid var(--green)}
.mainnav{left:0;top:3px;width:381px;height:21px;background:var(--panel-dark);display:flex;font-size:5.5px;color:#bbb}
.mainnav li{list-style:none;padding:7px 10px;border-right:1px solid #333}
.mainnav li.active{background:var(--green);color:#fff}
.slide{left:7px;top:29px;width:254px;height:142px;background:linear-gradient(135deg,#1b2a3a,#3c6a8c 55%,#15202b)}
.slide-cap{left:7px;top:143px;width:254px;height:28px;background:rgba(0,0,0,.55);color:#fff;padding:5px 8px}
.slide-cap b{font-size:7px;font-weight:600;display:block}
.side{left:266px;top:29px;width:108px}
.side h4{font-size:6px;color:#fff;padding:4px;background:var(--panel-dark)}
.side .thumb1{height:52px;background:#3a2e24;padding:4px;display:flex;gap:4px;color:#ddd}
.side .thumb1 i{width:48px;height:40px;background:linear-gradient(#7a5a3a,#4a3020);display:block;flex:none}
.side .thumb2{height:72px;margin-top:4px;background:linear-gradient(135deg,#3a2a20,#1a1410)}
.section-h{font-size:7px;font-weight:700;color:#fff}
.cards{left:7px;top:210px;display:flex;gap:6px}
.card{width:87px}
.card .ph{height:72px}
.card p{color:#ddd;font-size:6px;margin:6px 0 4px}
.card .row{display:flex;justify-content:space-between;align-items:center;color:#999;font-size:4.5px}
.btn{background:var(--green);color:#fff;font-size:4.5px;font-weight:700;padding:2px 6px;display:inline-block}
.content{left:196px;top:396px;width:381px;height:594px;background:#f7f7f7}
.box{background:#fff;position:absolute}
.h-green{font-size:7px;color:#555;padding:6px 7px;border-bottom:1px solid #e4e4e4}
.h-green em{font-style:normal;color:var(--green)}
.post{left:0;width:261px;height:128px}
.post .meta{left:8px;top:14px;width:64px;font-size:5px;color:#777;line-height:1.6}
.post .date{background:#e6e6e6;padding:3px 5px;margin-bottom:6px;color:#555}
.post .meta span{color:var(--green)}
.post h3{left:75px;top:1px;font-size:7px;font-weight:400;color:#444}
.post .ph{left:75px;top:14px;width:175px;height:56px;background:linear-gradient(135deg,#1a2636,#3d6b90 55%,#0d151e)}
.post p{left:75px;top:74px;width:175px;font-size:4.5px;color:#666}
.post .btn{right:8px;bottom:8px;position:absolute}
.right{left:462px;width:109px}
.tabs{display:flex;font-size:5px;border-bottom:1px solid #ddd}
.tabs span{padding:4px 7px}
.tabs .on{background:#fff;border:1px solid #ddd;border-bottom:none}
.wlist{list-style:none;font-size:5px;padding:3px 8px}
.wlist li{padding:4px 0;border-bottom:1px solid #eee;color:#666;display:flex;gap:4px;align-items:center}
.wlist li::before{content:"";width:3px;height:3px;border-radius:50%;background:var(--orange);flex:none}
.wlist li.on{color:var(--green)}
.promo{background:var(--orange);color:#fff;text-align:center;padding-top:8px}
.promo-kicker{font-size:4.5px;font-weight:600}
.promo-title{font-size:10px;font-weight:700;line-height:1.1}
.promo-sub{font-size:5px;margin-top:2px}
.promo-btn{margin:6px 10px 0;background:var(--blue);font-size:6px;font-weight:700;padding:3px}
.footer{left:0;top:1003px;width:780px;height:197px;background:#1c1c1c;color:#aaa}
.fh{font-size:5.5px;color:#fff;font-weight:700;padding-bottom:4px;border-bottom:1px solid #333;width:105px}
.fsoc{left:372px;top:182px;display:flex;gap:2px}
.fsoc span{width:7px;height:7px;background:#444;display:block}
</style>
</head>
<body>

<svg class="abs hero-bg" viewBox="0 0 780 270" role="img" aria-label="Blurred football goal net on a grass pitch">
  <defs><linearGradient id="grass" x1="0" y1="0" x2="0" y2="1"><stop offset="0" stop-color="#6fae4a"/><stop offset=".6" stop-color="#3d8a2a"/><stop offset="1" stop-color="#2c6b1e"/></linearGradient></defs>
  <rect width="780" height="270" fill="url(#grass)"/>
  <path d="M0 200 Q390 200 780 200 L780 270 L0 270 Z" fill="none"/>
  <path d="M0 175 Q390 300 780 175 L780 270 L0 270 Z" fill="#ececec"/>
</svg>

<div class="abs topbar"></div>
<div class="abs topnav"><span class="active">Home</span><span>Most Popular</span><span>Top Stories</span><span>Custom Links</span></div>
<div class="abs social"><span></span><span></span><span></span><span></span></div>

<div class="abs brand"><span class="brand-dot"></span><span class="brand-name">Pitchside Talk</span></div>

<div class="abs panel">
  <ul class="abs mainnav"><li>ARTICLE</li><li>BLOGS</li><li class="active">MATCHES</li><li>VIDEOS</li><li>USEFUL LINK</li><li>LINKS</li></ul>
  <div class="abs slide" role="img" aria-label="Footballer striking a ball in a splash of water"></div>
  <div class="abs slide-cap"><b>Lorem Ipsum is simply dummy text of the printing and typesetting</b><span style="font-size:4.5px;color:#ccc">◷ 29 July 2014</span></div>
  <div class="abs side">
    <h4>NEWS UPDATE</h4>
    <div class="thumb1"><i role="img" aria-label="Player portrait"></i><span style="font-size:4.5px">Lorem Ipsum is simply<br>◷ 23 July 2014</span></div>
    <div class="thumb2" role="img" aria-label="Football boot advertisement"></div>
  </div>
  <div class="abs section-h" style="left:7px;top:190px">TODAY FEATURED STORE</div>
  <div class="abs cards">
    <div class="card"><div class="ph" role="img" aria-label="Fan in a jersey" style="background:linear-gradient(#a07048,#5a3a24)"></div><p>Lorem Ipsum is simply</p><div class="row"><span>◷ 12 AUG 2014</span><span class="btn">MORE</span></div></div>
    <div class="card"><div class="ph" role="img" aria-label="Player in a cap" style="background:linear-gradient(#6a6a6a,#3a2a2a)"></div><p>Lorem Ipsum is simply</p><div class="row"><span>◷ 12 AUG 2014</span><span class="btn">MORE</span></div></div>
    <div class="card"><div class="ph" role="img" aria-label="Leather jacket and gear" style="background:linear-gradient(#8a5a3a,#2a1a14)"></div><p>Lorem Ipsum is simply</p><div class="row"><span>◷ 12 AUG 2014</span><span class="btn">MORE</span></div></div>
    <div class="card"><div class="ph" role="img" aria-label="City street at dusk" style="background:linear-gradient(#5a5a5a,#1a1a1a)"></div><p>Lorem Ipsum is simply</p><div class="row"><span>◷ 12 AUG 2014</span><span class="btn">MORE</span></div></div>
  </div>
</div>

<div class="abs content">
  <div class="box" style="left:6px;top:6px;width:255px;height:32px;background:linear-gradient(90deg,#333,#2a2a2a);color:#fff">
    <div class="abs" role="img" aria-label="Electronics devices" style="left:4px;top:3px;width:70px;height:26px;background:linear-gradient(90deg,#8cc63f,#5a8a2a)"></div>
    <div class="abs" style="left:84px;top:3px;font-size:9px;font-weight:700;color:#8cc63f">SAVE UP TO 55%</div>
    <div class="abs" style="left:84px;top:15px;font-size:4.5px">ON ALL ELECTRONICS<br>-BEST QUALITY -BEST RATES -BEST DEALS</div>
    <div class="abs" style="left:178px;top:8px;background:#c8d630;color:#222;font-size:4.5px;font-weight:700;padding:3px 6px">CHECK OUT<br>TODAY'S DEALS</div>
  </div>

  <div class="box" style="left:0;top:44px;width:261px;height:12px"><div class="h-green" style="border:none;padding:2px 7px">LATEST <em>NEWS</em></div></div>

  <div class="box post" style="top:60px">
    <h3 class="abs">Lorem Ipsum is simply dummy text of the printing</h3>
    <div class="abs meta"><div class="date">▦ 25 JULY 2014</div>Author : <span>Kestrel Media</span><br>Comments : <span>08</span><br>Category : <span>Lorem Ipsum</span></div>
    <div class="abs ph" role="img" aria-label="Footballer kicking a ball"></div>
    <p class="abs">Lorem Ipsum is simply dummy text of the printing and typesetting industry. Lorem Ipsum has been the industry's standard dummy text ever since the 1500s, when an unknown printer took a galley of type and scrambled it.</p>
    <span class="btn">› more</span>
  </div>
  <div class="box post" style="top:198px">
    <h3 class="abs">Lorem Ipsum is simply dummy text of the printing</h3>
    <div class="abs meta"><div class="date">▦ 25 JULY 2014</div>Author : <span>Kestrel Media</span><br>Comments : <span>08</span><br>Category : <span>Lorem Ipsum</span></div>
    <div class="abs ph" role="img" aria-label="Footballer kicking a ball"></div>
    <p class="abs">Lorem Ipsum is simply dummy text of the printing and typesetting industry. Lorem Ipsum has been the industry's standard dummy text ever since the 1500s, when an unknown printer took a galley of type and scrambled it.</p>
    <span class="btn">› more</span>
  </div>

  <div class="box" style="left:0;top:336px;width:261px;height:130px">
    <div class="h-green">HOT <em>LIST</em></div>
    <div class="abs" role="img" aria-label="Woman in a fan shirt" style="left:5px;top:20px;width:105px;height:62px;background:linear-gradient(#c8b090,#6a5040)"></div>
    <div class="abs" style="left:5px;top:38px;width:24px;height:30px;background:#333;color:#fff;text-align:center;font-size:10px;font-weight:700;padding-top:2px">10<br><span style="font-size:4px">AUG</span></div>
    <div class="abs" style="left:5px;top:88px;width:105px;font-size:5px;font-weight:600;color:#333">Lorem Ipsum is simply dummy text of the printing and typesetting</div>
    <span class="btn abs" style="left:5px;top:108px">READ MORE</span>
    <div class="abs" style="left:120px;top:20px;width:138px">
      <div style="display:flex;gap:6px;height:34px"><i role="img" aria-label="Thumbnail" style="width:44px;height:28px;background:#7a6050;display:block;flex:none"></i><span style="font-size:5px">Lorem Ipsum is simply dummy text of the printing<br><span style="color:#999;font-size:4px">◷ 23 July 2014 | Comments (38)</span></span></div>
      <div style="display:flex;gap:6px;height:34px"><i role="img" aria-label="Thumbnail" style="width:44px;height:28px;background:#7a6050;display:block;flex:none"></i><span style="font-size:5px;color:var(--green)">Lorem Ipsum is simply dummy text of the printing<br><span style="color:#999;font-size:4px">◷ 23 July 2014 | Comments (38)</span></span></div>
      <div style="display:flex;gap:6px;height:34px"><i role="img" aria-label="Thumbnail" style="width:44px;height:28px;background:#7a6050;display:block;flex:none"></i><span style="font-size:5px">Lorem Ipsum is simply dummy text of the printing<br><span style="color:#999;font-size:4px">◷ 23 July 2014 | Comments (38)</span></span></div>
    </div>
  </div>

  <div class="box" style="left:0;top:480px;width:261px;height:114px">
    <div class="h-green">ARTICAL <em>POST</em></div>
    <div class="abs" style="left:7px;top:22px;display:flex;gap:6px">
      <div style="width:78px"><div role="img" aria-label="DNA strand" style="height:44px;background:linear-gradient(135deg,#0a2a30,#1f8a8a)"></div><p style="font-size:5px;margin-top:5px">Who Says The Waves Aren't Better On The Other Side!</p><p style="font-size:4px;color:#999;margin-top:6px">◷ 13 May 2014 | <span style="color:var(--green)">8 Replies</span></p></div>
      <div style="width:78px"><div role="img" aria-label="Open book pages" style="height:44px;background:linear-gradient(135deg,#4a6fa0,#c8d4e4)"></div><p style="font-size:5px;margin-top:5px">Who Says The Waves Aren't Better On The Other Side!</p><p style="font-size:4px;color:#999;margin-top:6px">◷ 13 May 2014 | <span style="color:var(--green)">8 Replies</span></p></div>
      <div style="width:78px"><div role="img" aria-label="Sunny field landscape" style="height:44px;background:linear-gradient(135deg,#f0d080,#a8c060)"></div><p style="font-size:5px;margin-top:5px;color:var(--green)">Who Says The Waves Aren't Better On The Other Side!</p><p style="font-size:4px;color:#999;margin-top:6px">◷ 13 May 2014 | <span style="color:var(--green)">8 Replies</span></p></div>
    </div>
  </div>

  <div class="box right" style="left:266px;top:6px;height:150px;background:#2a2a2a;color:#ddd;padding:7px">
    <div class="section-h" style="font-size:5.5px">VIDEO GALLERY</div>
    <div role="img" aria-label="Person celebrating outdoors" style="height:54px;margin:6px 0;background:linear-gradient(#7ab0d8,#c8d8e0)"></div>
    <p style="font-size:5px;color:#fff">Lorem Ipsum is simply dummy text of the printing and typesetting</p>
    <p style="font-size:4px;color:#999;margin-top:3px">Lorem Ipsum is simply dummy text of the printing and typesetting industry. Lorem Ipsum has been the industry's standard.</p>
    <span class="btn" style="margin-top:6px">READ MORE</span>
  </div>

  <div class="box right" style="left:266px;top:162px;height:114px">
    <div class="h-green" style="font-size:5.5px">WIDGET LIST</div>
    <div class="tabs"><span class="on">Popular</span><span>Recent</span><span>Archives</span></div>
    <ul class="wlist"><li>This 3-Year-Old Skates Better Than</li><li>This Is How You Exit The Highway</li><li>10 DIY Life Hacks for Camping</li><li class="on">This 3-Year-Old Skates</li><li>Old Skates Better Than Most Teens!</li></ul>
  </div>

  <div class="box right promo" style="left:266px;top:288px;height:90px">
    <div class="promo-kicker">THE SUPER HANDY</div>
    <div class="promo-title">WEEKEND<br>PUZZLE BOOK</div>
    <div class="promo-sub">of joy</div>
    <div class="promo-btn">FREE DOWNLOAD</div>
  </div>
</div>

<footer class="abs footer">
  <div class="abs" style="left:196px;top:20px">
    <div class="fh">POST WIDGET</div>
    <div style="display:flex;gap:6px;margin-top:10px"><i role="img" aria-label="Thumbnail" style="width:32px;height:26px;background:#5a6a7a;display:block;flex:none"></i><span style="font-size:5px;width:90px">Lorem Ipsum is simply dummy<br><span style="font-size:4px;color:#888">Lorem Ipsum is simply dummy text of the printing and typesetting industry.</span></span></div>
    <div style="display:flex;gap:6px;margin-top:10px"><i role="img" aria-label="Thumbnail" style="width:32px;height:26px;background:#5a6a7a;display:block;flex:none"></i><span style="font-size:5px;width:90px;color:var(--green)">Lorem Ipsum is simply dummy<br><span style="font-size:4px;color:#888">Lorem Ipsum is simply dummy text of the printing and typesetting industry.</span></span></div>
  </div>
  <div class="abs" style="left:360px;top:20px">
    <div class="fh">DEMO POST</div>
    <div role="img" aria-label="Eagle soaring in the sky" style="width:121px;height:46px;margin-top:10px;border:3px solid #fff;background:linear-gradient(#3a78c8,#8ab8e8)"></div>
    <p style="font-size:4.5px;width:121px;margin-top:6px">Lorem Ipsum is simply dummy text of the printing and typesetting industry. <span style="color:var(--green)">Learn More</span></p>
  </div>
  <div class="abs" style="left:520px;top:20px">
    <div class="fh" style="width:58px">SITE INFO</div>
    <ul style="list-style:none;font-size:4.5px;line-height:1.8;margin-top:8px"><li>› Log In</li><li>› My Account</li><li>› Blog Post</li><li>› Video</li><li>› Entries RSS</li></ul>
  </div>
  <div class="abs" style="left:196px;top:138px;width:381px;border-top:1px solid #333"></div>
  <p class="abs" style="left:226px;top:148px;width:328px;text-align:center;font-size:4.5px">Lorem Ipsum is simply dummy text of the printing and typesetting industry. Lorem Ipsum has been the industry's standard dummy text ever since the 1500s, when an unknown printer took a galley of type and scrambled it to make a type specimen book.</p>
  <p class="abs" style="left:196px;top:168px;width:381px;text-align:center;font-size:4.5px">© 2014 Company Name. All rights reserved.</p>
  <div class="abs fsoc"><span></span><span></span><span></span><span></span><span></span><span></span><span></span><span></span></div>
</footer>

</body>
</html>
```